TORV graphic design elements

TORV is a group of schools who have adopted positive psychology as the framework for their wellbeing programs.

Designs should be simple and formal (rather than ultra modern/trendy)

I require quotes for the following:
Letterhead
Business Card
Powerpoint slides
Pull up banner (approx 2m high)
Colour pallette development

I have uploaded a copy of our logo

```html
<!DOCTYPE html>
<html lang="en">
<head>
<meta charset="utf-8">
<title>TORV Letterhead</title>
<link href="https://fonts.googleapis.com/css2?family=Open+Sans:wght@400;700&display=swap" rel="stylesheet">
<style>
  :root {
    --backdrop: #e7e4e0;
    --paper: #ffffff;
    --brand-orange: #f68d21;
    --brand-blue: #1f74b9;
    --on-orange: #ffffff;
  }
  * { box-sizing: border-box; margin: 0; padding: 0; }
  html, body {
    width: 1200px;
    height: 1000px;
    overflow: hidden;
    background: var(--backdrop);
    font-family: "Open Sans", Arial, sans-serif;
  }
  .letterhead {
    position: absolute;
    left: 275px;
    top: 40px;
    width: 650px;
    height: 920px;
    background: var(--paper);
    box-shadow: 0 6px 22px rgba(0, 0, 0, 0.18);
  }
  .brand {
    position: absolute;
    left: 44px;
    top: 44px;
    display: flex;
    align-items: center;
    gap: 12px;
  }
  .brand-mark {
    width: 34px;
    height: 34px;
    border-radius: 50%;
    background: var(--brand-orange);
  }
  .brand-name {
    font-weight: 700;
    font-size: 44px;
    line-height: 1;
    letter-spacing: 0.5px;
    color: var(--brand-blue);
  }
  .contact-band {
    position: absolute;
    left: 270px;
    right: 0;
    top: 36px;
    height: 54px;
    background: var(--brand-orange);
    display: flex;
    align-items: center;
    padding-left: 44px;
  }
  .phone {
    color: var(--on-orange);
    font-size: 13px;
    letter-spacing: 1.2px;
  }
  .address-band {
    position: absolute;
    left: 0;
    right: 0;
    bottom: 0;
    height: 172px;
    background: var(--brand-orange);
  }
  .address {
    position: absolute;
    left: 24px;
    bottom: 18px;
    font-style: normal;
    color: var(--on-orange);
    font-size: 12px;
    line-height: 17px;
    letter-spacing: 1.2px;
  }
</style>
</head>
<body>
  <main class="letterhead">
    <header>
      <div class="brand">
        <span class="brand-mark"></span>
        <span class="brand-name">TORV</span>
      </div>
      <div class="contact-band">
        <p class="phone">ph. 0800.555.014</p>
      </div>
    </header>
    <footer class="address-band">
      <address class="address">
        Linden Street No. 48<br>
        North Valley<br>
        East Province<br>
        20814
      </address>
    </footer>
  </main>
</body>
</html>
```